Webdesign für Vertrieb und Verkauf von Quintora Produkten im Firmenbereich
Zielgruppe
Vertrieb und Verkauf von Quintora Produkten im Firmenbereich (Quintora LEX, Trade Pilot)
Aufgabenstellung
Ein Logo gibt es auf der bestehenden Internetseite https://www.veloxware.eu/ - Dieses Logo bitte beibehalten.
Ansonsten eine schnörkelloses klares Design welches Firmenkunden anspricht und wo man sich schnell zurecht findet.

```html
<!DOCTYPE html>
<html lang="de">
<head>
<meta charset="utf-8">
<title>Meine Vorteile – Velox</title>
<link href="https://fonts.googleapis.com/css2?family=Fira+Sans:wght@400;500;600;700&display=swap" rel="stylesheet">
<style>
:root{
  --accent:#a8184a;
  --ink:#141414;
  --text:#6b6b6b;
  --panel:#f5f5f5;
  --line:#e6e6e6;
  --footer:#000;
  --footer-card:#1c1c1c;
  --footer-bar:#141414;
  --white:#fff;
}
*{box-sizing:border-box;margin:0;padding:0}
html,body{width:1200px;height:2288px;overflow:hidden}
body{position:relative;background:var(--white);font-family:"Fira Sans",Arial,sans-serif;color:var(--text);font-size:11px;line-height:16px}
.abs{position:absolute}

/* header */
.site-header{left:0;top:0;width:1200px;height:62px;border-bottom:1px solid var(--line);background:var(--white)}
.brand{left:215px;top:20px;font-size:17px;letter-spacing:2px;color:#555;font-weight:400;display:flex;align-items:center;gap:6px}
.brand-dot{width:10px;height:10px;background:var(--accent);border-radius:50%}
.divider{top:0;width:1px;height:62px;background:var(--line)}
.main-nav{left:674px;top:25px;display:flex;gap:16px;font-size:9.5px;font-weight:600;color:#333}
.main-nav .current{color:var(--accent)}
.burger{left:971px;top:27px;width:13px}
.burger i{display:block;height:1.5px;background:#333;margin-bottom:2.5px}

/* hero */
.hero{left:0;top:62px;width:1200px;height:222px;background:linear-gradient(90deg,#c9c9c9 0%,#e4e4e4 30%,#d6d4d2 60%,#b9b5b2 85%,#a9a6a4 100%)}
.hero-mark{left:515px;top:80px;width:165px;height:175px;background:radial-gradient(ellipse at center,rgba(200,110,140,.55) 0%,rgba(200,110,140,.25) 55%,rgba(200,110,140,0) 75%)}
.hero-title{left:0;top:218px;width:1200px;text-align:center;font-size:20px;font-weight:600;color:var(--ink)}

/* sections */
.section-title{left:0;width:1200px;text-align:center;font-size:16.5px;font-weight:600;color:var(--ink)}
.panel{left:216px;width:770px;background:var(--panel)}
.photo-band{left:0;top:952px;width:1200px;height:604px;background:linear-gradient(180deg,#e9e9e9 0%,#dcdcdc 45%,#cfcfcf 80%,#e8e4e0 100%)}
.intro{left:228px;width:746px;text-align:center;font-size:10.3px;line-height:16.3px}

.card{width:170px;background:var(--white);border-top:3px solid var(--accent);border-bottom:3px solid var(--accent);box-shadow:0 1px 6px rgba(0,0,0,.08);padding:10px 11px 0 10px}
.card-head{display:flex;align-items:flex-start;gap:8px;font-size:10px;font-weight:600;color:var(--ink);line-height:16px;min-height:32px}
.card-head svg{flex:none;width:20px;height:22px;stroke:var(--accent);fill:none;stroke-width:1.2}
.card-head span{padding-top:5px}
.checks{list-style:none;margin-top:6px;font-size:10px;line-height:16px}
.checks li{position:relative;padding-left:12px}
.checks li::before{content:"";position:absolute;left:1px;top:5px;width:6px;height:3px;border-left:1.8px solid var(--accent);border-bottom:1.8px solid var(--accent);transform:rotate(-45deg)}

.acc{left:238px;font-size:10px;font-weight:600;color:var(--ink);display:flex;align-items:center;gap:8px}
.acc b{display:inline-block;width:8px;color:var(--accent);font-size:13px;font-weight:700;text-align:center}
.acc-text{left:238px;width:730px;font-size:10.2px;line-height:16.3px}

/* footer */
.site-footer{left:0;top:1978px;width:1200px;height:249px;background:var(--footer)}
.footer-card{left:216px;top:1972px;width:371px;height:181px;background:var(--footer-card);border-top:6px solid var(--accent)}
.footer-brand{left:241px;top:2018px;font-size:17px;letter-spacing:2px;color:#ddd;display:flex;align-items:center;gap:6px}
.footer-about{left:241px;top:2048px;width:330px;color:#9a9a9a;font-size:10px;line-height:16px}
.f-head{font-size:10px;font-weight:600;color:var(--white)}
.social{left:613px;top:2048px;list-style:none}
.social li{display:flex;align-items:center;gap:7px;height:24px;margin-bottom:5px;color:#ddd;font-size:10px}
.social i{display:block;width:24px;height:24px;background:#222}
.links{left:745px;top:2049px;width:107px;list-style:none}
.links li{font-size:9.5px;font-weight:600;color:var(--white);padding:4px 0 5px;border-bottom:1px solid #2a2a2a}
.links li:last-child{border-bottom:0}
.contact{left:877px;top:2017px;width:120px;color:var(--white);font-size:10px;line-height:16px}
.bottom-bar{left:0;top:2227px;width:1200px;height:61px;background:var(--footer-bar)}
.copyright{left:216px;top:2260px;font-size:8.5px;color:#bbb}
.copyright u{color:#ddd}
.to-top{left:956px;top:2250px;width:29px;height:29px;border:1px solid #555}
</style>
</head>
<body>

<header class="site-header abs"></header>
<div class="brand abs"><span class="brand-dot"></span>VELOX</div>
<div class="divider abs" style="left:293px"></div>
<div class="divider abs" style="left:950px"></div>
<nav class="main-nav abs"><span>Home</span><span>Was ist Quintora LEX?</span><span class="current">Meine Vorteile</span><span>Kontakt</span></nav>
<div class="burger abs"><i></i><i></i><i></i></div>

<section class="hero abs" role="img" aria-label="Unscharfes Foto einer Hand mit erhobenem Daumen als Hintergrund"></section>
<div class="hero-mark abs" role="img" aria-label="Großes Pokal-Symbol in Rosa"></div>
<h1 class="hero-title abs">Meine Vorteile</h1>

<!-- Bessere Kontrolle -->
<h2 class="section-title abs" style="top:337px">Bessere Kontrolle</h2>
<div class="panel abs" style="top:386px;height:500px"></div>
<p class="intro abs" style="top:395px">Um das richtige Maß an Kontrolle zu erhalten, benötigen Sie ein System, das nicht nur Ihre Entscheidungen durch jederzeit aktuelle Informationen über die Unternehmensleistung unterstützt, sondern das alle Prozesse in einer durchgängig produktiven Arbeitsumgebung zusammenführt. Mit Quintora LEX können Sie sich darauf verlassen, dass jeder Mitarbeiter geeignete Werkzeuge erhält, um schneller zu handeln und die richtigen Entscheidungen zu treffen. Zudem können Sie alle Aspekte Ihrer Geschäftstätigkeit überwachen und auswerten – von der Kapazitäts- und Ressourcenplanung über die Bestandsverwaltung bis zum Versand.</p>

<div class="card abs" style="left:241px;top:492px;height:220px">
  <div class="card-head"><svg viewBox="0 0 20 22"><rect x="2" y="9" width="4" height="12"/><rect x="8" y="2" width="4" height="19"/><rect x="14" y="13" width="4" height="8"/></svg><span>Finanzmanagement</span></div>
  <ul class="checks"><li>Effiziente Buchführung</li><li>Cashflow-Management</li><li>Verwaltung von Anlagen<br><br>Währungen,Standorten und Mandanten</li><li>Effiziente Buchführung</li></ul>
</div>
<div class="card abs" style="left:424px;top:492px;height:220px">
  <div class="card-head"><svg viewBox="0 0 22 22"><circle cx="11" cy="11" r="3.5"/><circle cx="11" cy="11" r="8" stroke-dasharray="3 2"/></svg><span>Fertigung</span></div>
  <ul class="checks"><li>Steuerung von Produktionsaufträgen</li><li>Vorratsplanung</li><li style="margin-top:5px">Kapazitätsplanung</li></ul>
</div>
<div class="card abs" style="left:607px;top:492px;height:220px">
  <div class="card-head"><svg viewBox="0 0 22 22"><rect x="2" y="11" width="10" height="5" rx="2.5" transform="rotate(-45 7 13.5)"/><rect x="10" y="5" width="10" height="5" rx="2.5" transform="rotate(-45 15 7.5)"/></svg><span>Supply Chain<br><br>Management</span></div>
  <ul class="checks" style="margin-top:20px"><li>Genehmigungsprozesse</li><li style="margin-top:5px">Verwaltung von Lager- und Bestandsdaten</li><li>Analyse von Kundenbedarf</li><li>Effektive Zusammenarbeit mit Partnern</li><li>Steuerung der Lieferkette</li></ul>
</div>
<div class="card abs" style="left:789px;top:492px;height:220px">
  <div class="card-head"><svg viewBox="0 0 20 22"><path d="M10 2a6 6 0 0 1 3.5 10.9V16h-7v-3.1A6 6 0 0 1 10 2z"/><path d="M7 18h6M8 20h4"/></svg><span>Berichtswesen</span></div>
  <ul class="checks"><li>Budgetverwaltung</li><li>Assistentengeführte individuelle</li><li style="margin-top:5px">Konsolidierung und Auswertung von Finanzdaten</li><li>Verfolgung von Trends und Beziehungen</li></ul>
</div>

<div class="acc abs" style="top:742px"><b>–</b>Bessere Abläufe</div>
<p class="acc-text abs" style="top:774px">Je nach der Position („Rolle“), die ein Mitarbeiter in Ihrem Unternehmen ausfüllt, erhält er über so genannte Rollencenter eine individuell gestaltete Benutzeroberfläche, die alle für ihn wichtigen Informationen und Aufgaben umfasst. Dies sorgt für effektiveres und produktiveres Arbeiten.</p>
<div class="acc abs" style="top:823px"><b>+</b>Klare Übersicht über Ihre Finanzdaten</div>
<div class="acc abs" style="top:853px"><b>+</b>Self-Service-Berichtswerkzeuge und Business Intelligence in Echtzeit</div>

<!-- Höhere Margen -->
<div class="photo-band abs" role="img" aria-label="Unscharfes Foto eines Schreibtischs mit Tastatur und Notizen"></div>
<h2 class="section-title abs" style="top:980px">Höhere Margen</h2>
<div class="panel abs" style="top:1030px;height:462px"></div>
<p class="intro abs" style="top:1039px">Wenn Sie schnelle, fundierte Entscheidungen treffen können, wirkt sich dies direkt auf Ihren Umsatz aus. Mit Quintora LEX können Sie wichtige Geschäftsprozesse durchgängig automatisieren, vom Einkauf über die Lagerverwaltung bis hin zu Verkauf und Service. So erhalten Sie Echtzeitinformationen aus allen Abteilungen, die Sie als Entscheidungsgrundlage nutzen können, um Kosten zu senken und Ihren Cashflow zu verbessern.</p>

<div class="card abs" style="left:241px;top:1104px;height:217px">
  <div class="card-head"><svg viewBox="0 0 24 22"><path d="M3 8h5l10-5v15L8 13H3z"/><path d="M6 13l2 6h3l-2-6"/></svg><span>Marketing und Vertrieb</span></div>
  <ul class="checks"><li>Effektive Verwaltung von Kunden-und Verkaufsdaten</li><li>Kampagnenverwaltung</li><li>Pipeline-und Verkaufschancesteuerung</li><li>Lieferterminzusagen</li><li>Durchgängige Auftragsverwaltung</li></ul>
</div>
<div class="card abs" style="left:424px;top:1104px;height:217px">
  <div class="card-head"><svg viewBox="0 0 24 22"><rect x="1" y="5" width="22" height="14"/><path d="M8 5V2h8v3M1 11h22"/></svg><span>Personalverwaltung</span></div>
  <ul class="checks"><li>Erfassung und Verwaltung von Mitarbeiterstammdaten</li><li>Kommentare für Personalakten</li><li>Erfassung von Fehlzeiten</li><li>Berichtserstellung</li></ul>
</div>
<div class="card abs" style="left:607px;top:1104px;height:217px">
  <div class="card-head"><svg viewBox="0 0 24 22"><rect x="1" y="2" width="22" height="14"/><path d="M12 16v4M7 20h10"/></svg><span>Servicemanagement</span></div>
  <ul class="checks"><li>Verwaltung von Kundenanrufen und-anfragen</li><li>Verfolgung von Support-Tickets</li><li>Einsatzplanung für Serviceressourcen</li><li>Bedarfsplanung für Ersatzteile</li><li>Verwaltung von Verträgen und Servicevereinbarungen</li></ul>
</div>
<div class="card abs" style="left:789px;top:1104px;height:217px">
  <div class="card-head"><svg viewBox="0 0 24 22"><path d="M1 4h8l2 2h12v14H1z"/><path d="M1 9h22"/></svg><span>Projektmamagement</span></div>
  <ul class="checks"><li>Budgetierung nach Kosten und Zeitaufwand</li><li>Automatisierung von Abrechnungen</li><li>Verfolgung von Ressourcenkosten und-verbrauch</li><li>Kapazitätsplanung</li><li>Verfügbarkeitsprognosen</li></ul>
</div>

<div class="acc abs" style="top:1348px"><b>–</b>Topkunden und neue Verkaufschancen identifizieren</div>
<p class="acc-text abs" style="top:1381px">Mithilfe von Analysen und Forecasts können Sie neue Verkaufschancen bei Ihren besten Kunden ermitteln und sich gezielt auf Ihre rentabelsten Produkte konzentrieren, um Ihre Geschäftsergebnisse zu verbessern.</p>
<div class="acc abs" style="top:1430px"><b>+</b>Kundenbindung mit individuellen Preisen und Rabatten</div>
<div class="acc abs" style="top:1459px"><b>+</b>Besserer Kundenservice mit effizienter Serviceauftragsverwaltung</div>

<!-- Mehr Wachstum -->
<h2 class="section-title abs" style="top:1606px">Mehr Wachstum</h2>
<div class="panel abs" style="top:1656px;height:253px"></div>
<p class="intro abs" style="top:1665px">Sie und Ihre Mitarbeiter haben eine gemeinsame Vision: Den langfristigen Erfolg Ihres Unternehmens. Das richtige Maß an Unterstützung erhalten Sie dabei durch eine Lösung, die jederzeit an neue und veränderte Anforderungen angepasst werden kann. Quintora LEX ist flexibel, trägt neuen Geschäftsprozessen Rechnung und wächst mit Ihrem Unternehmen – budget- und ressourcenschonend.</p>
<div class="acc abs" style="top:1765px"><b>–</b>Internationale Geschäfte</div>
<p class="acc-text abs" style="top:1798px">Mit den Funktionen für den internationalen Handel und der Mehrwährungsfähigkeit können Sie für beliebig viele Währungen festlegen, wie Beträge gerundet und gebucht werden sollen, und Sie können Kunden- und Lieferantenkonten in der passenden Währung verwalten.</p>
<div class="acc abs" style="top:1847px"><b>+</b>Produktive, ortsunabhängige Zusammenarbeit</div>
<div class="acc abs" style="top:1876px"><b>+</b>Die richtige Lösung für Ihr Unternehmen</div>

<!-- footer -->
<footer class="site-footer abs"></footer>
<div class="footer-card abs"></div>
<div class="footer-brand abs"><span class="brand-dot"></span>VELOX</div>
<p class="footer-about abs">Viele unterschiedliche Projekte und Kunden durfte VELOX in den letzten 5 Jahren europaweit betreuen. Mit 11 Jahren Gesamterfahrung im Quintora LEX Umfeld, ist kein Projekt zu klein oder zu kompliziert für uns.</p>

<div class="f-head abs" style="left:613px;top:2015px">Soziale Netzwerke</div>
<ul class="social abs"><li><i></i>Kurznachrichten</li><li><i></i>Netzwerk</li><li><i></i>Berufsnetz</li></ul>

<div class="f-head abs" style="left:745px;top:2015px">Links</div>
<ul class="links abs"><li>Home</li><li>Was ist Quintora LEX?</li><li>Meine Vorteile</li><li>Kontakt</li></ul>

<div class="contact abs">Sie haben Fragen oder möchten einen Termin vereinbaren?<br><br><br><b style="font-weight:600">info@veloxware.eu</b><br><br><b style="font-weight:600">Velox GmbH</b><br>Lindenweg 14 - 90402<br>Nürnberg</div>

<div class="bottom-bar abs"></div>
<div class="copyright abs">© 2015 - 2018 Velox GmbH. <u>Impressum</u> | <u>Datenschutz</u></div>
<svg class="to-top abs" viewBox="0 0 29 29"><path d="M10 17l4.5-4.5L19 17" fill="none" stroke="#bbb" stroke-width="1.5"/></svg>

</body>
</html>
```